We need motivational posters designed to be used in classrooms at a truck driving school. The purpose of the posters is to motivate the students.

I want the the quotes to be the main focal point of emphasis and our logo on the bottom of the poster for branding purposes.

I would like the images to be related to the trucking industry

Below are the quotes for the posters

Poster 1
"Start where you are. Use what you have. Do what you can."
-Delmar Quisby-

Poster 2
"The secret of getting ahead is getting started"
-Owen Farrow-

Poster 3
"Most effective way to do it, is to do it."
-Rosalind Pemberly-

Poster 4
"Set your goals big, and don't stop till you get there."
-Cy Whitlock-

Poster 5
"If you are not willing to learn, no one can help you. If you are determined to learn, no one can stop you."
-Unknown-

Poster 6
"The will to succeed is important, but what's more important is the will to prepare."
-Dougie Hallam-

THESE POSTERS SHOULD BE DESIGNED AS 18X24
LANDSCAPE AND PORTRAIT ORIENTATION

Industry/Entity Type

School

```html
<!DOCTYPE html>
<html lang="en">
<head>
<meta charset="utf-8">
<title>Set your goals big – Summit Truck Driving School</title>
<link href="https://fonts.googleapis.com/css2?family=Anton&family=Open+Sans:ital,wght@0,800;1,800&display=swap" rel="stylesheet">
<style>
  :root {
    --poster-yellow: #fff200;
    --poster-yellow-light: #fffbb0;
    --quote-red: #ee1c25;
    --outline-white: #ffffff;
    --ink-black: #111111;
    --truck-red: #d8123a;
    --trailer-white: #f4f4f4;
    --logo-gold: #e2a21a;
  }
  * { margin: 0; padding: 0; box-sizing: border-box; }
  html, body { width: 898px; height: 1200px; overflow: hidden; }
  .poster {
    position: relative;
    width: 898px;
    height: 1200px;
    background: linear-gradient(to bottom, var(--poster-yellow) 0%, var(--poster-yellow) 62%, var(--poster-yellow-light) 100%);
    overflow: hidden;
  }
  .quote {
    position: absolute;
    top: 28px;
    left: 0;
    width: 100%;
    text-align: center;
    font-family: "Anton", "Oswald", sans-serif;
    font-size: 104px;
    line-height: 153px;
    letter-spacing: -1px;
    color: var(--quote-red);
    -webkit-text-stroke: 14px var(--outline-white);
    paint-order: stroke fill;
  }
  .quote-line { display: block; white-space: nowrap; }
  .quote-line--first { margin-left: -28px; }
  .quote-line--last { margin-left: -44px; }
  .attribution {
    position: absolute;
    top: 470px;
    right: 22px;
    font-family: "Open Sans", Arial, sans-serif;
    font-style: italic;
    font-weight: 800;
    font-size: 50px;
    color: var(--ink-black);
    -webkit-text-stroke: 8px var(--outline-white);
    paint-order: stroke fill;
    white-space: nowrap;
  }
  .truck-photo {
    position: absolute;
    left: 54px;
    top: 540px;
    width: 812px;
    height: 515px;
  }
  .brand-block {
    position: absolute;
    left: 30px;
    top: 1047px;
    width: 409px;
    height: 128px;
    background: var(--outline-white);
    display: flex;
    align-items: center;
    gap: 14px;
    padding: 0 18px;
  }
  .brand-mark {
    flex: none;
    width: 92px;
    height: 92px;
    border-radius: 50%;
    background: var(--logo-gold);
  }
  .brand-name {
    font-family: "Open Sans", Arial, sans-serif;
    font-weight: 800;
    font-size: 21px;
    line-height: 1.15;
    color: var(--logo-gold);
    text-transform: uppercase;
  }
</style>
</head>
<body>
  <main class="poster">
    <h1 class="quote">
      <span class="quote-line quote-line--first">"Set your goals big,</span>
      <span class="quote-line">and don't stop</span>
      <span class="quote-line quote-line--last">till you get there."</span>
    </h1>
    <p class="attribution">-Cy Whitlock-</p>

    <svg class="truck-photo" role="img" aria-label="Photo of a red semi truck cab pulling a white refrigerated trailer" viewBox="0 0 812 515" preserveAspectRatio="none">
      <defs>
        <linearGradient id="truck-tones" x1="0" y1="0" x2="1" y2="0">
          <stop offset="0" stop-color="var(--trailer-white)"/>
          <stop offset="0.42" stop-color="#e6e6e6"/>
          <stop offset="0.55" stop-color="var(--truck-red)"/>
          <stop offset="1" stop-color="#b80f30"/>
        </linearGradient>
      </defs>
      <rect x="0" y="0" width="812" height="515" rx="18" fill="url(#truck-tones)"/>
    </svg>

    <div class="brand-block">
      <span class="brand-mark" aria-hidden="true"></span>
      <p class="brand-name">Summit Truck Driving School, LLC</p>
    </div>
  </main>
</body>
</html>
```